New Wordpress, web design and a logo for a text analysis website. The website name is Quorvela.com

Task Description- We are looking for an exciting design for a new textual analysis website in Wordpress. The website enables individuals (initially only academics, but this might be expanded later) to upload textual data (e.g. excel files) for processing and download textual analysis results. For example, users can upload data with hundreds of Excel cells containing text and receive back analysis of the positive/negative sentiment in that text, the count of complex words, the count of numbers, the most frequent terms, or similarity of text in the uploaded database. The landing page will explain the concept and vision of the website, will perhaps visually illustrate the ease with which it can be done (files uploaded and results downloaded with no need for technical knowledge). Hence, we want to communicate that we provide an easy to use, yet powerful tool. Although we do not have images to share, we would like the website to include images and graphic images, you may use stock images in your design.

Logo- The design should include a logo with the word “Quorvela” and perhaps a magnifying glass enlarging text, but we are open to some creative thinking of the logo. Overall, we are hoping to communicate the following terms: “textual analysis” and “analytics”.
Pages- The design should include at least the following pages (each should include a logo, header, body, background, navigation menu and a footer)

1. Home page, describing the overall objective to enable easy analysis of textual data. The background/images should likely illustrate text going into a magnifying glass/a computer/ or another automation-related and graphs (pie chart, bar chart, etc.), or other outputs, are coming out of the other side. We are open to all other creative suggestions to illustrate this process.
2. Tools- this page will list the different textual analysis tools that the website is offering and briefly explain each. Each of these tools is a link to its own page where the tool can be applied. Examples of tools that will be included are (1) Count of words and numbers (2) sentiment analysis (3) custom uploaded dictionary of words analysis (4) Similarity analysis (5) N-gram analysis of frequent single or multiple words.
3. Design of one tool page (we will replicate the design ourselves for other tools)- Each page will include an explanation of the procedure and files the users should prepare. Each page should also include forms that allow the users to (1) Browse their computer to upload their text file (2) drop down select boxes (3) radio buttons or check boxes. We will change the number of these boxes ourselves in the future.
4. Registration/Login- a standard registration page, asking users for name (first and last), email, set a password and confirm it. And also, allowing existing users to login.
5. About page- a page that includes information about the two researchers, including a photo and a short text describing their background.
6. News- a page describing news and media mentions of the page and links to research papers that used the tool.
Colors- The project is developed by researchers from two universities and the colors of both schools should be incorporated into the design. The primary colors of red and blue should be prominent. The color codes are in the following links (1) https://brand.halvermoor.edu/guide/design-elements/colors/ (2) https://www.ostrander.edu/offices/marketing-communications/ostrander-brand/brand-assets/ostrander-color-palette

Quorvela

```html
<!DOCTYPE html>
<html lang="en">
<head>
<meta charset="utf-8">
<title>Quorvela – Text Analysis</title>
<link href="https://fonts.googleapis.com/css2?family=Nunito:wght@600;700;800&family=Roboto:wght@400;500;700&display=swap" rel="stylesheet">
<style>
  :root{
    --blue:#1466b8;
    --blue-deep:#0f4f9e;
    --red:#d71920;
    --navy:#0d2158;
    --ink:#2b2b2b;
    --muted:#555b66;
    --pale:#dfe7f0;
    --card:#eef1f5;
    --white:#ffffff;
  }
  *{margin:0;padding:0;box-sizing:border-box}
  html,body{width:1200px;height:3856px;overflow:hidden}
  body{position:relative;background:var(--white);font-family:"Roboto",Arial,sans-serif;color:var(--ink)}
  .abs{position:absolute}
  .heading{font-family:"Nunito",Arial,sans-serif;font-weight:800;color:var(--blue);white-space:nowrap}
  .brand{font-family:"Nunito",Arial,sans-serif;font-weight:800;color:var(--white);display:flex;align-items:center;gap:12px;white-space:nowrap}
  .brand-dot{width:34px;height:34px;border-radius:50%;background:var(--white)}
  .btn{display:flex;align-items:center;justify-content:center;background:var(--red);color:var(--white);border-radius:20px;font-size:12px;font-weight:700;letter-spacing:.3px}
  p.body{font-size:14.5px;line-height:19px;color:var(--muted);white-space:nowrap}

  /* hero */
  .hero{left:0;top:0;width:1200px;height:686px;
    background:
      radial-gradient(ellipse 170px 260px at 230px 470px,rgba(30,24,22,.85) 0%,rgba(30,24,22,0) 100%),
      radial-gradient(ellipse 190px 200px at 250px 560px,rgba(255,255,255,.95) 0%,rgba(255,255,255,0) 100%),
      radial-gradient(ellipse 200px 130px at 500px 420px,rgba(90,150,210,.9) 0%,rgba(90,150,210,0) 100%),
      radial-gradient(ellipse 190px 150px at 700px 460px,rgba(40,110,200,.9) 0%,rgba(40,110,200,0) 100%),
      radial-gradient(ellipse 500px 90px at 600px 640px,rgba(245,245,245,.95) 0%,rgba(245,245,245,0) 100%),
      linear-gradient(100deg,#8f9b8b 0%,#b9c1bb 25%,#9aa0a4 45%,#3b3f45 62%,#1d1f23 100%)}
  .nav a{position:absolute;top:46px;color:var(--white);text-decoration:none;font-size:15px;font-weight:500;white-space:nowrap}
  .nav .active::after{content:"";position:absolute;left:0;right:0;bottom:-7px;height:2px;background:#4aa3ff}
  .hero-title{left:615px;width:400px;top:162px;text-align:center;font-family:"Nunito",Arial,sans-serif;font-weight:800;font-size:62px;line-height:80px;color:var(--white)}
  .hero-sub{left:615px;width:400px;top:250px;text-align:center;font-size:16px;font-weight:700;line-height:21px;color:var(--white)}

  /* cards */
  .card{background:var(--card)}
  .card .shot{width:100%;height:181px}
  .card h3{position:absolute;left:31px;font-family:"Nunito",Arial,sans-serif;font-weight:700;font-size:20px;color:var(--ink);white-space:nowrap}
  .card p{position:absolute;left:32px;font-size:13px;line-height:18px;color:var(--muted);white-space:nowrap}
  .card .date{position:absolute;left:31px;font-size:14px;color:var(--red)}

  .res-links a{position:absolute;left:0;color:var(--blue);font-size:14px;font-weight:500;text-decoration:none;white-space:nowrap}
  .tool-links a{position:absolute;left:26px;color:var(--white);font-size:16px;text-decoration:underline;white-space:nowrap}
  .tool-links span{position:absolute;left:0;color:var(--white);font-size:15px}

  /* footer */
  .footer{left:0;top:3470px;width:1200px;height:386px;background:var(--navy);color:var(--white)}
  .footer h4{position:absolute;font-size:14px;font-weight:700;letter-spacing:.3px}
  .footer ul{position:absolute;list-style:none;font-size:13px;line-height:24px}
  .social{position:absolute;width:27px;height:27px;border:1.5px solid var(--white);border-radius:50%}
</style>
</head>
<body>

<!-- Hero -->
<div class="abs hero" role="img" aria-label="Photo of an analyst at a desk pointing at charts on two monitors"></div>
<div class="abs brand" style="left:172px;top:34px;font-size:40px"><span class="brand-dot"></span>Quorvela</div>
<nav class="abs nav" style="left:0;top:0;width:1200px">
  <a class="active" style="left:533px">HOME</a>
  <a style="left:622px">TOOLS&#8964;</a>
  <a style="left:726px">REGISTRATION</a>
  <a style="left:881px">ABOUT</a>
  <a style="left:979px">NEWS</a>
</nav>
<h1 class="abs hero-title">Quorvela</h1>
<p class="abs hero-sub">Lorem ipsum dolor sit amet, consectetur<br>adipiscing elit, sed do eiusmod tem</p>

<!-- Recent Analysis -->
<h2 class="abs heading" style="left:172px;top:816px;font-size:36px">Recent Analysis</h2>
<p class="abs body" style="left:172px;top:877px">Lorem ipsum dolor sit amet, consecteloretur<br>adipiscing elit, sed do eiusmod tempor iloc<br>ididunt ut labore et dolore magna aliqua.lotr<br>Ut enim ad minim veniam, quis nostrud lor<br>exercitation ullamco laboris nisi ut alloiquip<br>ex ea commodo consequatuis aute irure do<br>lor in reprehenderit in voluptmodo cons</p>
<div class="abs btn" style="left:172px;top:1033px;width:128px;height:39px">READ MORE</div>
<div class="abs" role="img" aria-label="Illustration of a tablet with floating bar and line charts"
  style="left:509px;top:770px;width:561px;height:390px;background:
    radial-gradient(ellipse 150px 110px at 200px 140px,rgba(30,100,200,.75) 0%,rgba(30,100,200,0) 100%),
    radial-gradient(ellipse 110px 130px at 330px 110px,rgba(110,170,230,.7) 0%,rgba(110,170,230,0) 100%),
    radial-gradient(ellipse 90px 120px at 420px 100px,rgba(80,160,230,.55) 0%,rgba(80,160,230,0) 100%),
    radial-gradient(ellipse 280px 70px at 290px 280px,rgba(60,70,90,.55) 0%,rgba(60,70,90,0) 100%),
    radial-gradient(ellipse 300px 90px at 290px 260px,rgba(205,215,228,1) 0%,rgba(205,215,228,0) 100%),
    radial-gradient(ellipse 290px 190px at 290px 200px,#e3eef9 0%,rgba(255,255,255,0) 100%)"></div>

<!-- About -->
<div class="abs" style="left:0;top:1224px;width:1200px;height:567px;background:var(--pale)"></div>
<div class="abs" role="img" aria-label="Photo of hands typing on a laptop showing dashboard charts"
  style="left:0;top:1224px;width:720px;height:567px;background:
    radial-gradient(ellipse 190px 200px at 440px 230px,rgba(250,252,255,1) 0%,rgba(250,252,255,0) 100%),
    radial-gradient(ellipse 45px 45px at 455px 240px,rgba(40,120,200,.9) 0%,rgba(40,120,200,0) 100%),
    radial-gradient(ellipse 160px 60px at 320px 390px,rgba(225,190,175,.85) 0%,rgba(225,190,175,0) 100%),
    radial-gradient(ellipse 130px 330px at 40px 330px,rgba(28,38,62,1) 0%,rgba(28,38,62,0) 100%),
    linear-gradient(90deg,#3a4a66 0%,#a9b7c8 25%,#cdd8e4 60%,var(--pale) 100%)"></div>
<h2 class="abs heading" style="left:721px;top:1386px;font-size:36px">About Quorvela</h2>
<p class="abs body" style="left:721px;top:1449px">Lorem ipsum dolor sit amet, consecteloretur<br>adipiscing elit, sed do eiusmod tempor iloc<br>ididunt ut labore et dolore magna aliqua.lotr<br>Ut enim ad minim veniam, quis nostrud lor<br>exercitation ullamco laboris nisi ut alloiquip<br>ex ea commodo consequatuis aute irure do<br>lor in reprehenderit in voluptmodo cons</p>
<div class="abs btn" style="left:721px;top:1602px;width:128px;height:39px">READ MORE</div>

<!-- Researchers -->
<h2 class="abs heading" style="left:171px;top:1914px;font-size:36px">Researchers</h2>
<p class="abs body" style="left:171px;top:1976px">Lorem ipsum dolor sit amet, consectur<br>adipiscing elit, sed do eiusmompor</p>
<div class="abs res-links" style="left:171px;top:2046px">
  <a style="top:0">Lorem ipsum dolor sit ame</a>
  <a style="top:31px">consectetur adipiscing elit.</a>
  <a style="top:62px">Gravida orci eu ipsum</a>
  <a style="top:93px">malesuada, in imperdiet</a>
  <a style="top:124px">urna accumsan.</a>
  <a style="top:155px">Praesent lacinia ipsum</a>
</div>
<div class="abs card" style="left:486px;top:1905px;width:271px;height:381px">
  <div class="shot" role="img" aria-label="Photo of a researcher reading a document through a magnifying glass" style="background:radial-gradient(ellipse 90px 60px at 150px 110px,rgba(240,240,245,.9) 0%,rgba(240,240,245,0) 100%),linear-gradient(135deg,#1c2c4a,#34476a 60%,#5d7090)"></div>
  <h3 style="top:234px">Loremporroisqua</h3>
  <p style="top:275px">Lorem ipsum dolor sit amet,<br>consecteloretur adipiscing elit,<br>sed do eiusmod tempor</p>
</div>
<div class="abs card" style="left:787px;top:1905px;width:271px;height:381px">
  <div class="shot" role="img" aria-label="Photo of a magnifying glass over a laptop keyboard and screen" style="background:radial-gradient(ellipse 60px 60px at 190px 100px,rgba(235,240,248,.95) 0%,rgba(235,240,248,0) 100%),linear-gradient(160deg,#5a6f9a,#2d3448 60%,#c9d2de)"></div>
  <h3 style="top:234px">Loremporroisqua</h3>
  <p style="top:275px">Lorem ipsum dolor sit amet,<br>consecteloretur adipiscing elit,<br>sed do eiusmod tempor</p>
</div>

<!-- Tools banner -->
<div class="abs" style="left:139px;top:2379px;width:923px;height:327px;background:var(--blue)"></div>
<div class="abs" role="img" aria-label="Photo of a magnifying glass over printed charts and data tables"
  style="left:560px;top:2379px;width:502px;height:327px;background:
    radial-gradient(ellipse 110px 110px at 210px 150px,rgba(240,245,250,.95) 0%,rgba(240,245,250,0) 100%),
    radial-gradient(ellipse 70px 60px at 370px 110px,rgba(220,70,60,.45) 0%,rgba(220,70,60,0) 100%),
    radial-gradient(ellipse 60px 50px at 220px 290px,rgba(200,60,60,.45) 0%,rgba(200,60,60,0) 100%),
    linear-gradient(90deg,var(--blue) 0%,#5b95cf 30%,#d8e3ee 60%,#f3f5f8 100%)"></div>
<h2 class="abs" style="left:177px;top:2440px;font-family:'Nunito',Arial,sans-serif;font-weight:800;font-size:36px;color:var(--white);white-space:nowrap">Quorvela Tools</h2>
<div class="abs tool-links" style="left:172px;top:2511px">
  <span style="top:0">&raquo;</span><a style="top:0">Count of words and numbers</a>
  <span style="top:25px">&raquo;</span><a style="top:25px">Sentiment analysis</a>
  <span style="top:50px">&raquo;</span><a style="top:50px">Custom uploaded dictionary of words analysis</a>
  <span style="top:75px">&raquo;</span><a style="top:75px">Similarity analysis</a>
  <span style="top:100px">&raquo;</span><a style="top:100px">N-gram analysis of frequent single or multiple words</a>
</div>

<!-- Latest News -->
<div class="abs" style="left:0;top:2834px;width:1200px;height:636px;background:var(--pale)"></div>
<h2 class="abs heading" style="left:0;width:1200px;top:2908px;text-align:center;font-size:36px">Latest News</h2>
<div class="abs card" style="left:165px;top:3004px;width:271px;height:382px;background:#f1f3f6">
  <div class="shot" role="img" aria-label="Photo of a magnifying glass over printed bar charts" style="background:radial-gradient(ellipse 70px 50px at 110px 110px,rgba(60,70,110,.6) 0%,rgba(60,70,110,0) 100%),linear-gradient(135deg,#c9a9a9,#b8bcc8 50%,#e3e6ec)"></div>
  <span class="date" style="top:210px">Dec 18 2020</span>
  <h3 style="top:244px">Loremporroisqua</h3>
  <p style="top:287px">Lorem ipsum dolor sit amet,<br>consecteloretur adipiscing elit,<br>sed do eiusmod tempor</p>
</div>
<div class="abs card" style="left:464px;top:3004px;width:271px;height:382px;background:#f1f3f6">
  <div class="shot" role="img" aria-label="Photo of a team reviewing printed reports on a table" style="background:radial-gradient(ellipse 110px 70px at 150px 110px,rgba(225,230,238,.9) 0%,rgba(225,230,238,0) 100%),linear-gradient(135deg,#2c3d5c,#7e8ea8 50%,#c8d2de)"></div>
  <span class="date" style="top:210px">Dec 18 2020</span>
  <h3 style="top:244px">Loremporroisqua</h3>
  <p style="top:287px">Lorem ipsum dolor sit amet,<br>consecteloretur adipiscing elit,<br>sed do eiusmod tempor</p>
</div>
<div class="abs card" style="left:763px;top:3004px;width:271px;height:382px;background:#f1f3f6">
  <div class="shot" role="img" aria-label="Photo of hands holding a tablet showing charts" style="background:radial-gradient(ellipse 90px 60px at 170px 90px,rgba(110,160,210,.8) 0%,rgba(110,160,210,0) 100%),linear-gradient(135deg,#b59a88,#8d98aa 50%,#d2dce8)"></div>
  <span class="date" style="top:210px">Dec 18 2020</span>
  <h3 style="top:244px">Loremporroisqua</h3>
  <p style="top:287px">Lorem ipsum dolor sit amet,<br>consecteloretur adipiscing elit,<br>sed do eiusmod tempor</p>
</div>

<!-- Footer -->
<footer class="abs footer">
  <div class="brand" style="position:absolute;left:169px;top:100px;font-size:36px"><span class="brand-dot" style="width:30px;height:30px"></span>Quorvela</div>
  <span class="social" style="left:212px;top:166px"></span>
  <span class="social" style="left:248px;top:166px"></span>
  <span class="social" style="left:284px;top:166px"></span>
  <span class="social" style="left:320px;top:166px"></span>

  <h4 style="left:449px;top:82px">ABOUT US</h4>
  <ul style="left:449px;top:114px">
    <li>Sed ut perspiciatis</li><li>Unde omnis iste natus</li><li>Voluptatem accusan</li><li>Tium doloremque</li><li>Haudantium</li><li>Tum doloremque</li>
  </ul>

  <h4 style="left:670px;top:82px">NEWSLETTER</h4>
  <p style="position:absolute;left:670px;top:116px;font-size:13px;line-height:19px;white-space:nowrap">Subscribe to us to get and<br>receive the latest news, sales<br>and updates.</p>
  <span style="position:absolute;left:670px;top:190px;font-size:11px;font-style:italic">Email Address:</span>
  <span style="position:absolute;left:670px;top:217px;width:166px;height:1px;background:#5a6a95"></span>
  <div class="btn" style="position:absolute;left:670px;top:236px;width:100px;height:36px;font-size:13px;font-weight:500">SIGN UP</div>

  <h4 style="left:899px;top:82px">LINKS</h4>
  <ul style="left:899px;top:114px">
    <li>Sed ut perspiciatis</li><li>Unde omnis iste natus</li><li>Voluptatem accusan</li><li>Tium doloremque</li><li>Haudantium</li><li>Tum doloremque</li>
  </ul>

  <span style="position:absolute;left:148px;top:305px;width:880px;height:1px;background:#2c3f78"></span>
  <p style="position:absolute;left:0;width:1200px;top:334px;text-align:center;font-size:13px">© 2020 All rights are reserved. Privacy | Terms of use</p>
</footer>

</body>
</html>
```